Easy one-page Web Design with ready made sketch/template

This project have an already made one page Web Design sketch/template that should be used as a base. It needs professional touch and improvements but should be quite straight forward for you to make.

Webpage: Offers local graphical design services

Attached following documents for you:
- PSD sketch
- JPG sketch
- Word file with project description (read carefully)
- Logo

Reason: Project extended to get the final designs submitted. Thanks

Target Market(s)

Logo design

Industry/Entity Type

Graphic Design

Number of Pages Required

1 page

Requirements
Must have
• Please refer to attached word document.
Nice to have
Should not have

```html
<!DOCTYPE html>
<html lang="sv">
<head>
<meta charset="utf-8">
<title>Märkesverket – Ny logotyp</title>
<link href="https://fonts.googleapis.com/css2?family=Roboto:wght@300;400;500;700&family=Open+Sans:wght@400;600;700&display=swap" rel="stylesheet">
<style>
:root{
  --blue:#2a9fd8;
  --orange:#e67e22;
  --yellow:#fdb94a;
  --green:#2f8a1f;
  --ink:#222;
  --muted:#555;
  --panel:#f1f1f1;
  --header:#ececec;
  --stage:#1c1c1c;
}
*{box-sizing:border-box;margin:0;padding:0}
html,body{width:1200px;height:1200px;overflow:hidden;background:var(--stage)}
.page{position:absolute;left:300px;top:0;width:703px;height:1408px;background:#fff;transform:scale(.8523);transform-origin:0 0;font-family:"Open Sans",sans-serif;color:var(--ink);overflow:hidden}
.abs{position:absolute}
.site-header{left:0;top:0;width:703px;height:72px;background:var(--header)}
.brand{left:28px;top:24px;display:flex;align-items:center;gap:6px;font-family:"Roboto",sans-serif;font-size:16px;font-weight:500;color:var(--blue)}
.brand-dot{width:12px;height:12px;background:var(--blue)}
.nav{left:228px;top:29px;display:flex;gap:11px;font-family:"Roboto",sans-serif;font-size:11px}
.order-btn{left:434px;top:20px;width:110px;height:32px;background:var(--blue);color:#fff;font-family:"Roboto",sans-serif;font-size:9.5px;display:flex;align-items:center;justify-content:center;gap:8px}
.phone{left:557px;top:27px;font-family:"Roboto",sans-serif;font-size:12.5px;letter-spacing:.3px}
.hero{left:0;top:72px;width:703px;height:403px;background:radial-gradient(ellipse at 50% 45%,#ffffff 0%,#f2f2f2 45%,#c9c9c9 75%,#7d7d7d 100%)}
.hero-title{left:0;top:176px;width:703px;text-align:center;font-family:"Roboto",sans-serif;font-size:26px;font-weight:400;letter-spacing:.5px}
.hero-sub{left:170px;top:217px;width:363px;text-align:center;font-family:"Roboto",sans-serif;font-size:12px;line-height:16px;color:var(--muted)}
.how-btn{left:284px;top:271px;width:135px;height:34px;border:2px solid var(--blue);border-radius:17px;display:flex;align-items:center;justify-content:center;gap:8px;font-family:"Roboto",sans-serif;font-size:12.5px;background:#fff}
.start{left:0;top:343px;width:703px;text-align:center;font-family:"Roboto",sans-serif;font-size:16px}
.start span{color:var(--blue)}
.badge{color:#fff;text-align:center;font-family:"Roboto",sans-serif}
.badge-guarantee{left:30px;top:424px;width:194px;height:109px;background:var(--yellow)}
.badge-order{left:224px;top:407px;width:256px;height:143px;background:var(--orange)}
.badge-order:after{content:"";position:absolute;left:112px;bottom:-16px;border-left:16px solid transparent;border-right:16px solid transparent;border-top:16px solid var(--orange)}
.badge-rating{left:480px;top:424px;width:193px;height:109px;background:var(--green)}
.section-title{left:0;width:703px;text-align:center;font-family:"Roboto",sans-serif;font-size:22px;font-weight:400;letter-spacing:1px;color:#333}
.section-sub{left:0;width:703px;text-align:center;font-family:"Roboto",sans-serif;font-size:15px;letter-spacing:1px;color:var(--blue)}
.plan{background:var(--panel);font-family:"Open Sans",sans-serif}
.plan-head{height:30px;background:var(--blue);color:#fff;font-size:12px;font-weight:700;letter-spacing:.8px;display:flex;align-items:center;justify-content:center}
.plan-price{text-align:center;color:var(--blue);font-size:18px;font-weight:700;letter-spacing:1px;padding-top:4px;line-height:22px}
.plan-vat{text-align:center;font-size:8px;color:#444;padding-bottom:10px;border-bottom:1px solid #fff}
.plan ul{list-style:none;padding:10px 0 0 18px}
.plan li{position:relative;padding-left:12px;font-size:8px;line-height:15px}
.plan li:before{content:"";position:absolute;left:0;top:5px;width:5px;height:5px;border-radius:50%;background:var(--blue)}
.plan-cta{position:absolute;left:0;width:100%;text-align:center;font-size:8px;line-height:15px}
.plan-btn{position:absolute;height:22px;background:var(--blue);color:#fff;font-size:8px;font-weight:700;display:flex;align-items:center;justify-content:center;letter-spacing:.5px}
.plan-featured .plan-head{height:35px;background:var(--orange);font-size:13px}
.plan-featured .plan-price{color:var(--orange);font-size:20px;padding-top:6px}
.plan-featured li{font-size:9.5px;line-height:18px}
.plan-featured li:before{top:7px}
.review-photo{left:15px;top:1183px;width:181px;height:148px;background:linear-gradient(135deg,#e8e8e8,#d2d2d2)}
.review{width:175px;font-family:"Open Sans",sans-serif}
.review-stars{display:flex;gap:2px}
.review-stars i{width:10px;height:10px;background:#1b8f3a;display:block}
.review-date{position:absolute;right:0;top:1px;font-size:5.5px;color:#aaa}
.review h4{font-size:9.5px;font-weight:700;margin-top:10px;letter-spacing:.3px}
.review p{font-size:8.5px;line-height:11px;margin-top:8px;color:#333}
.review .author{position:absolute;top:84px;font-size:8.5px;font-weight:700}
.arrow{font-family:"Roboto",sans-serif;font-size:20px;color:#999}
</style>
</head>
<body>
<div class="page">
  <header class="abs site-header">
    <div class="abs brand"><span class="brand-dot"></span>Märkesverket</div>
    <nav class="abs nav"><span>Products</span><span>Gallery</span><span>FAQ</span><span>Contact us</span></nav>
    <div class="abs order-btn">
      <svg width="16" height="13" viewBox="0 0 16 13"><path d="M0 1h3l2 7h8l2-5H5" fill="none" stroke="#fff" stroke-width="1.6"/><circle cx="6" cy="11" r="1.3" fill="#fff"/><circle cx="12" cy="11" r="1.3" fill="#fff"/></svg>
      ORDER LOGO
    </div>
    <div class="abs phone">Ring 08-555 01 23</div>
  </header>

  <section class="abs hero" role="img" aria-label="Foto ovanifrån av ett skrivbord med lampa, pennor, penslar och färgburkar"></section>
  <h1 class="abs hero-title">Ny Logotyp / Företagslogga?</h1>
  <p class="abs hero-sub">Neque porro quisquam est qui dolorem ipsum quia dolor sit amet, consectetur, adipisci velit..</p>
  <div class="abs how-btn">
    <svg width="16" height="16" viewBox="0 0 16 16"><circle cx="8" cy="8" r="8" fill="var(--blue)"/><path d="M6 4.5l5 3.5-5 3.5z" fill="#fff"/></svg>
    How it works
  </div>
  <p class="abs start">Start From <span>$1495</span></p>

  <div class="abs badge badge-guarantee">
    <svg class="abs" style="left:82px;top:12px" width="30" height="34" viewBox="0 0 30 34"><path d="M8 2h14v9a7 7 0 0 1-14 0zM8 5H3v3a5 5 0 0 0 5 5M22 5h5v3a5 5 0 0 1-5 5M15 18v7M9 31h12v-3H9z" fill="none" stroke="#fff" stroke-width="1.8"/></svg>
    <div class="abs" style="left:0;top:54px;width:194px;font-size:11px;font-weight:700;letter-spacing:.8px">NÖJDGARANTI</div>
    <div class="abs" style="left:0;top:70px;width:194px;font-size:16px;letter-spacing:1px">100%</div>
  </div>
  <div class="abs badge badge-order">
    <div class="abs" style="left:0;top:14px;width:256px;font-size:13px;letter-spacing:.5px">BESTÄLL LOGOTYP</div>
    <svg class="abs" style="left:102px;top:34px" width="54" height="54" viewBox="0 0 54 54">
      <path d="M27 4a23 23 0 1 1-16 39" fill="none" stroke="#fff" stroke-width="4"/>
      <path d="M6 36l5 8 7-5" fill="none" stroke="#fff" stroke-width="3"/>
      <g stroke="#fff" stroke-width="3"><path d="M20 6l1 3M12 12l2 2M6 21l3 1M4 30h3"/></g>
      <text x="27" y="34" text-anchor="middle" font-family="Roboto,sans-serif" font-weight="700" font-size="20" fill="#fff">24</text>
    </svg>
    <div class="abs" style="left:0;top:100px;width:256px;font-size:13px;letter-spacing:.8px">FRÅN 1495:-</div>
  </div>
  <div class="abs badge badge-rating">
    <svg class="abs" style="left:44px;top:12px" width="106" height="18" viewBox="0 0 106 18">
      <g fill="#fff">
        <path id="st" d="M9 0l2.6 5.8 6.4.6-4.8 4.2 1.4 6.3L9 13.6 3.4 16.9l1.4-6.3L0 6.4l6.4-.6z"/>
        <use href="#st" x="22"/><use href="#st" x="44"/><use href="#st" x="66"/><use href="#st" x="88"/>
      </g>
    </svg>
    <div class="abs" style="left:0;top:38px;width:193px;font-size:11.5px;font-weight:500">9/10 - Betygsätter UTMÄRKT</div>
    <div class="abs" style="left:0;top:56px;width:193px;font-size:10px">200+ omdömen</div>
    <div class="abs" style="left:60px;top:80px;width:72px;height:10px;background:rgba(255,255,255,.35)"></div>
  </div>

  <h2 class="abs section-title" style="top:592px">SELECT A PACKAGE</h2>
  <p class="abs section-sub" style="top:621px">FIXED PRICE!</p>

  <div class="abs plan" style="left:19px;top:705px;width:145px;height:291px">
    <div class="plan-head">STARTER</div>
    <div class="plan-price">1495/-</div>
    <div class="plan-vat">(+moms)</div>
    <ul><li>3 logotypputkast</li><li>1 ändring/revision</li><li>Filer för webben</li></ul>
    <div class="plan-cta" style="top:194px"><b>Beställ nu!</b><br><b>GRATIS</b> Profilbild-logga*</div>
    <div class="plan-btn" style="left:26px;top:241px;width:90px">BESTÄLL</div>
  </div>
  <div class="abs plan" style="left:170px;top:705px;width:148px;height:291px">
    <div class="plan-head">STARTER</div>
    <div class="plan-price">1495/-</div>
    <div class="plan-vat">(+moms)</div>
    <ul><li>3 logotypputkast</li><li>1 ändring/revision</li><li>Filer för webben</li></ul>
    <div class="plan-cta" style="top:194px"><b>Beställ nu!</b><br><b>GRATIS</b> Profilbild-logga*</div>
    <div class="plan-btn" style="left:26px;top:241px;width:90px">BESTÄLL</div>
  </div>
  <div class="abs plan plan-featured" style="left:321px;top:669px;width:172px;height:411px">
    <div class="plan-head">STARTER</div>
    <div class="plan-price">1495/-</div>
    <div class="plan-vat">(+moms)</div>
    <ul>
      <li>100% nöjdhetsgaranti</li><li>10 logotypputkast</li>
      <li style="line-height:12px;padding-bottom:4px;padding-top:2px">Obergränsat med ändringar /revisioner</li>
      <li>Allt du behöver ingår</li><li>Visitkort design</li><li>Brevpapper design</li>
      <li>Logotypguide</li><li>Telefonsupport</li><li>Profilbild logotyp</li>
      <li>Webb &amp; tryckfiler ingår</li>
      <li style="line-height:12px;padding-top:2px">BESTÄLL IDAG: Få en bonusprodukt (värde 495kr)</li>
    </ul>
    <div class="plan-cta" style="top:330px;font-size:9px;line-height:12px">Erbjudandet gäller<br>0d 23t 47min 30s</div>
    <div class="plan-btn" style="left:31px;top:364px;width:104px;height:25px;background:var(--orange)">BESTÄLL</div>
  </div>
  <div class="abs plan" style="left:496px;top:705px;width:149px;height:291px">
    <div class="plan-head">STARTER</div>
    <div class="plan-price">1495/-</div>
    <div class="plan-vat">(+moms)</div>
    <ul><li>3 logotypputkast</li><li>1 ändring/revision</li><li>Filer för webben</li></ul>
    <div class="plan-cta" style="top:194px"><b>Beställ nu!</b><br><b>GRATIS</b> Profilbild-logga*</div>
    <div class="plan-btn" style="left:26px;top:241px;width:90px">BESTÄLL</div>
  </div>

  <h2 class="abs section-title" style="top:1120px">CUSTOMER REVIEWS</h2>
  <p class="abs section-sub" style="top:1147px">RANKED #1</p>

  <div class="abs review-photo" role="img" aria-label="Foto av en nöjd kund som håller upp sin nya restauranglogotyp"></div>
  <div class="abs arrow" style="left:223px;top:1244px">‹</div>
  <div class="abs review" style="left:257px;top:1207px">
    <div class="review-stars"><i></i><i></i><i></i><i></i><i></i></div>
    <span class="review-date">Publicerat den 10 juli 2017</span>
    <h4>Snabbt och proffsigt utfört</h4>
    <p>Snabbt och proffsigt utfört, bra design, mycket nöjd</p>
    <span class="author">Nils Berg</span>
  </div>
  <div class="abs review" style="left:456px;top:1207px">
    <div class="review-stars"><i></i><i></i><i></i><i></i><i></i></div>
    <span class="review-date">Publicerat den 10 juli 2017</span>
    <h4>Snabb återkoppling och leverans</h4>
    <p>Snabb återkoppling och leverans! Vi är supernöjda med logotypen</p>
    <span class="author">Nils Berg</span>
  </div>
  <div class="abs arrow" style="left:657px;top:1244px">›</div>

  <h2 class="abs section-title" style="top:1356px;font-size:21px">WHY CHOOSE US?</h2>
  <p class="abs section-sub" style="top:1383px">100% SATISFACTION</p>
</div>
</body>
</html>
```